Webdesign für Hundeerziehungsberatung
Zielgruppe:
Hundehalter, die entweder einen Welpen angeschafft haben, ihren Hund ausbilden oder fördern wollen sowie Menschen mit einem 'Problemhund'.
Die Hundeerziehungsberatung bietet Hundehaltern die Erziehung im Einzelsetting und im Gruppensetting an.
Aufgabenstellung
die Farben sollen sich am Logo orientieren, gern noch eine Farbe dazu. Logo anbei, Bilder anbei. Flyer anbei
Sollten die Bilder ausreichen bitten wir um Auswahl bei pixel.morvani. Tool: Photoshop.
Der Kundin gefällt: https://www.pfotenlauf-brevik.de/

```html
<!DOCTYPE html>
<html lang="de">
<head>
<meta charset="utf-8">
<title>Pfotenwerk – Hundeschule Pfotenlauf</title>
<link href="https://fonts.googleapis.com/css2?family=Barlow+Condensed:wght@400;500&family=Arimo:wght@400&display=swap" rel="stylesheet">
<style>
:root{
  --taupe:#7b7062;
  --taupe-dark:#6e6457;
  --text:#8a8076;
  --muted:#9a938b;
  --line:#d9d4cf;
  --grey-bg:#ededed;
  --white:#fff;
  --head:"Barlow Condensed",sans-serif;
  --body:"Arimo",sans-serif;
}
*{box-sizing:border-box;margin:0;padding:0}
html,body{width:1200px;height:4580px;overflow:hidden;background:var(--white)}
body{position:relative;font-family:var(--body);color:var(--text)}
.abs{position:absolute}
.h-title{font-family:var(--head);font-weight:500;color:var(--taupe);text-align:center;font-size:40px;line-height:1;text-transform:uppercase}
.h-sub{font-family:var(--head);font-weight:400;color:var(--taupe);text-align:center;font-size:32px;line-height:1;text-transform:uppercase}

/* header */
.site-header{top:0;left:0;width:1200px;height:101px;display:flex;align-items:center;justify-content:center;gap:12px}
.brand-dot{width:50px;height:50px;border-radius:50%;border:3px solid var(--taupe)}
.brand-name{font-family:var(--head);font-size:40px;color:var(--taupe);font-weight:400}

/* hero */
.hero{top:101px;left:0;width:1200px;height:724px;background:linear-gradient(100deg,#8d7a55 0%,#a8916a 35%,#8c8a80 60%,#6f6e6a 100%)}
.main-nav{top:0;left:0;width:1200px;height:34px;background:rgba(90,85,75,.35);display:flex;gap:0;padding-left:92px}
.main-nav a{color:var(--white);font-family:var(--head);font-size:16px;text-decoration:none;line-height:34px;margin-right:19px}
.hero-title{left:92px;top:222px;width:510px;text-align:center;font-family:var(--head);font-weight:500;font-size:50px;line-height:62px;color:var(--white);letter-spacing:1px}
.btn-hero{top:395px;width:248px;height:66px;border:2px solid var(--white);border-radius:4px;color:var(--white);font-family:var(--head);font-size:17px;display:flex;align-items:center;justify-content:center}

/* offers */
.card{top:1060px;width:328px;height:538px;border:1px solid var(--line);padding:12px 10px}
.card-img{height:256px}
.card h3{font-family:var(--head);font-weight:500;font-size:19px;color:var(--taupe);text-align:center;margin:18px 0 12px;padding-bottom:12px;border-bottom:1px solid var(--line)}
.card p{font-size:13.5px;line-height:21px;text-align:justify;text-align-last:center;padding:0 6px;color:var(--muted)}
.btn-outline{display:flex;align-items:center;justify-content:center;border:2px solid var(--taupe);border-radius:3px;color:var(--taupe);font-family:var(--head);font-size:15px;height:50px}
.card .btn-outline{width:186px;margin:20px auto 0}

/* about */
.about{top:1720px;left:0;width:1200px;height:705px;background:linear-gradient(90deg,#4d5a2c 0%,#6b6a3c 40%,#5e6e36 70%,#4a5a2a 100%)}
.about-box{left:617px;top:0;width:508px;height:598px;background:var(--taupe);padding:55px 36px;color:var(--white);text-align:center}
.about-box .t{font-family:var(--head);font-weight:500;font-size:40px;line-height:1}
.about-box .s{font-family:var(--head);font-size:30px;line-height:1;margin:10px 0 36px}
.about-box p{font-size:13.5px;line-height:26px;text-align:justify;text-align-last:center;margin-bottom:22px}

/* team */
.team-img{left:92px;top:2640px;width:468px;height:525px;background:radial-gradient(ellipse at center,#c9b9a2 0%,#ddd2c3 55%,#fff 75%)}
.team-text{left:628px;top:2665px;width:497px}
.team-text h3{font-family:var(--head);font-weight:500;font-size:28px;color:var(--taupe);padding-bottom:12px;border-bottom:1px solid var(--line)}
.team-text .quote{font-size:21px;line-height:29px;margin:24px 0 20px;color:var(--muted)}
.team-text p{font-size:13.5px;line-height:26px;color:var(--muted);margin-bottom:24px}
.team-text .btn-outline{width:186px}

/* testimonials */
.reviews{top:3255px;left:0;width:1200px;height:635px;background:var(--grey-bg)}
.review{top:195px;width:328px;height:335px;border:1px solid #d6d2cd;padding:45px 26px 0}
.review .qm{position:absolute;top:-30px;left:0;width:100%;text-align:center;font-family:Georgia,serif;font-size:60px;line-height:60px;color:#a39a90;background:transparent}
.review p{font-size:14px;line-height:26px;color:var(--muted);text-align:justify}
.review .name{font-family:var(--head);font-size:20px;color:var(--taupe);text-align:center;margin-top:26px}
.dots{top:580px;left:0;width:1200px;display:flex;justify-content:center;gap:9px}
.dots span{width:10px;height:10px;border-radius:50%;background:#cfcac4}
.dots span:first-child{background:var(--taupe)}

/* newsletter */
.newsletter{top:3890px;left:0;width:1200px;height:120px;background:var(--taupe);color:var(--white)}
.nl-title{left:92px;top:28px;font-family:var(--head);font-weight:500;font-size:32px;line-height:30px}
.nl-text{left:364px;top:44px;font-size:13.5px;line-height:26px;width:360px}
.nl-input{left:781px;top:34px;width:344px;height:52px;border:2px solid var(--white);border-radius:3px;font-family:var(--head);font-size:17px;padding-left:14px;line-height:48px}

/* footer */
.f-head{top:4093px;font-family:var(--head);font-weight:500;font-size:25px;color:var(--taupe)}
.field{border:1px solid #b9b2aa;border-radius:3px;font-size:12px;color:#aaa;padding:12px 6px}
.f-links{left:562px;top:4145px;font-size:14px;line-height:35px;color:var(--muted);list-style:none}
.f-contact{left:866px;top:4150px;font-size:14px;color:var(--muted)}
.f-contact .row{display:flex;align-items:center;gap:14px;height:42px}
.social{width:40px;height:40px;border-radius:50%;background:var(--taupe)}
.send{left:92px;top:4452px;width:181px;height:50px;background:var(--taupe);border-radius:3px;color:var(--white);font-family:var(--head);font-size:22px;display:flex;align-items:center;justify-content:center}
.legal{right:75px;top:4470px;font-size:13.5px;color:var(--muted)}
</style>
</head>
<body>

<header class="site-header abs">
  <span class="brand-dot"></span>
  <span class="brand-name">Pfotenwerk</span>
</header>

<section class="hero abs" role="img" aria-label="Foto: Frau mit Brille hockt im herbstlichen Gras und schaut einem schwarz-weißen Hund ins Gesicht">
  <nav class="main-nav abs">
    <a>Home</a><a>Erstgespräch</a><a>Erziehung im Einzelsetting</a><a>Erziehung im Gruppensetting</a><a>Unternehmen</a><a>Veranstaltungen/News</a><a>Kurse/Termine</a><a>Kontakt</a>
  </nav>
  <h1 class="hero-title abs">HUNDESCHULE PFOTENLAUF<br>IN CHEMNITZ</h1>
  <div class="btn-hero abs" style="left:92px">GRUPPENSTUNDEN</div>
  <div class="btn-hero abs" style="left:351px">ERSTGESPRÄCH VEREINBAREN</div>
</section>

<h2 class="h-title abs" style="top:906px;left:0;width:1200px">Hund Pfotenlauf</h2>
<p class="h-sub abs" style="top:953px;left:0;width:1200px">Vielfältige Angebote warten auf dich</p>

<article class="card abs" style="left:92px">
  <div class="card-img" role="img" aria-label="Foto: zwei spielende Hunde springen über eine Wiese" style="background:linear-gradient(180deg,#8fa36a 0%,#7e8f52 55%,#6c9a3a 100%)"></div>
  <h3>EINZELCOACHING</h3>
  <p>Lorem ipsum dolor sit amet, consectetuer adipiscing elit. Aenean commodo ligula eget dolor. Aenean massa. Cum sociis natoque penatibus et magnis dis parturient montes</p>
  <div class="btn-outline">TERMIN VEREINBAREN</div>
</article>
<article class="card abs" style="left:448px">
  <div class="card-img" role="img" aria-label="Foto: heller Welpe läuft über eine Wiese" style="background:linear-gradient(180deg,#b9a57a 0%,#a89a6a 55%,#8a8a50 100%)"></div>
  <h3>EINZELCOACHING</h3>
  <p>Lorem ipsum dolor sit amet, consectetuer adipiscing elit. Aenean commodo ligula eget dolor. Aenean massa. Cum sociis natoque penatibus et magnis dis parturient montes</p>
  <div class="btn-outline">TERMIN VEREINBAREN</div>
</article>
<article class="card abs" style="left:798px">
  <div class="card-img" role="img" aria-label="Foto: zwei spielende Hunde springen über eine Wiese" style="background:linear-gradient(180deg,#8fa36a 0%,#7e8f52 55%,#6c9a3a 100%)"></div>
  <h3>EINZELCOACHING</h3>
  <p>Lorem ipsum dolor sit amet, consectetuer adipiscing elit. Aenean commodo ligula eget dolor. Aenean massa. Cum sociis natoque penatibus et magnis dis parturient montes</p>
  <div class="btn-outline">TERMIN VEREINBAREN</div>
</article>

<section class="about abs" role="img" aria-label="Foto: brauner Hund gibt einer Hand die Pfote auf einer Wiese">
  <div class="about-box abs">
    <div class="t">ÜBER AUSBILDUNG</div>
    <div class="s">VIELFÄLTIGE ANGEBOTE WARTEN</div>
    <p>Lorem ipsum dolor sit amet, consectetuer adipiscing elit. Aenean commodo ligula eget dolor. Aenean massa. Cum sociis natoque penatibus et magnis dis parturient montesLorem ipsum dolor sit amet, consectetuer adipiscing elit. Aenean commodo ligula eget dolor. Aenean massa. Cum sociis natoque penatibus et magnis dis parturient montes</p>
    <p>massa quis enim. Donec pede justo, fringilla vel, aliquet nec, vulputate eget, arcu. In enim justo, rhoncus ut, imperdiet a, venenatis vitae, justo. Nullam dictum felis eu pede mollis pretium. Integer tincidunt.Lorem ipsum dolor sit amet, consectetuer adipiscing elit. Aenean commodo ligula eget dolor. Aenean massa. Cum sociis natoque penatibus et magnis dis parturient montes</p>
  </div>
</section>

<h2 class="h-title abs" style="top:2486px;left:0;width:1200px">Das Team</h2>
<p class="h-sub abs" style="top:2532px;left:0;width:1200px">Vielfältige Angebote warten auf dich</p>

<div class="team-img abs" role="img" aria-label="Foto: Trainerin sitzt im Schneidersitz mit einem Husky-Welpen"></div>
<div class="team-text abs">
  <h3>LENA MARBACH</h3>
  <p class="quote">Lernen ist wie Rudern gegen den Strom.<br>Hört man damit auf, treibt man zurück.“</p>
  <p>Lorem ipsum dolor sit amet, consectetuer adipiscing elit. Aenean commodo ligula eget dolor. Aenean massa. Cum sociis natoque penatibus et magnis dis parturient montes</p>
  <p>Lorem ipsum dolor sit amet, consectetuer adipiscing elit. Aenean commodo ligula eget dolor. Aenean massa. Cum sociis natoque penatibus et magnis dis parturient montes</p>
  <div class="btn-outline">TERMIN VEREINBAREN</div>
</div>

<section class="reviews abs">
  <h2 class="h-title abs" style="top:60px;left:0;width:1200px">Den Weg als Ziel sehe</h2>
  <p class="h-sub abs" style="top:110px;left:0;width:1200px;font-size:38px">Kundenstimmen</p>
  <div class="review abs" style="left:92px"><div class="qm">“</div><p>Danke, lieber Jonas, für deine Ruhe, deine Geduld und Ausgeglichenheit sowie die vielen guten Tipps aus einer für mich anfangs ungewohnten Perspektive. Heute bin ich froh, dass ich mich darauf eingelassen habe, neue Wege in der Hundeerziehung zu gehen.</p><div class="name">Greta Holm</div></div>
  <div class="review abs" style="left:447px"><div class="qm">“</div><p>Danke, lieber Jonas, für deine Ruhe, deine Geduld und Ausgeglichenheit sowie die vielen guten Tipps aus einer für mich anfangs ungewohnten Perspektive. Heute bin ich froh, dass ich mich darauf eingelassen habe, neue Wege in der Hundeerziehung zu gehen.</p><div class="name">Greta Holm</div></div>
  <div class="review abs" style="left:797px"><div class="qm">“</div><p>Danke, lieber Jonas, für deine Ruhe, deine Geduld und Ausgeglichenheit sowie die vielen guten Tipps aus einer für mich anfangs ungewohnten Perspektive. Heute bin ich froh, dass ich mich darauf eingelassen habe, neue Wege in der Hundeerziehung zu gehen.</p><div class="name">Greta Holm</div></div>
  <div class="dots abs"><span></span><span></span><span></span></div>
</section>

<section class="newsletter abs">
  <div class="nl-title abs">UNSER<br>NEWSLETTER</div>
  <p class="nl-text abs" style="top:28px">Lorem ipsum dolor sit amet, consectetuer adipiscing elit. Aenean commodo ligula eget dolor.</p>
  <div class="nl-input abs">EMAIL
    <svg class="abs" style="right:14px;top:13px" width="14" height="24" viewBox="0 0 14 24"><path d="M2 2l10 10L2 22" fill="none" stroke="#fff" stroke-width="2"/></svg>
  </div>
</section>

<h3 class="f-head abs" style="left:92px">DU HAST EINE FRAGE?</h3>
<div class="field abs" style="left:92px;top:4150px;width:163px;height:50px">Vor-und Nachname*</div>
<div class="field abs" style="left:272px;top:4150px;width:163px;height:50px">Email*</div>
<div class="field abs" style="left:92px;top:4216px;width:343px;height:50px">Telefonnumer*</div>
<div class="field abs" style="left:92px;top:4282px;width:343px;height:88px">Nachricht</div>
<div class="abs" style="left:92px;top:4396px;width:20px;height:20px;border:1px solid #b9b2aa;border-radius:3px"></div>
<p class="abs" style="left:118px;top:4398px;width:330px;font-size:13.5px;line-height:23px;color:var(--muted)">Die Datenschutzerklärung wurden gelesen und hiermit bestätigt</p>
<div class="send abs">SENDEN</div>

<h3 class="f-head abs" style="left:562px">LINKS</h3>
<ul class="f-links abs">
  <li>Home</li><li>Erstgespräch</li><li>Erziehung im Einzelsetting</li><li>Erziehung im Gruppensetting</li><li>Unternehmen</li><li>Veranstaltungen/News</li><li>Kurse/Termine</li><li>Kontakt</li>
</ul>

<h3 class="f-head abs" style="left:866px">KONTAKT</h3>
<div class="f-contact abs">
  <div style="font-weight:bold;color:var(--taupe);margin-bottom:10px">Pfotenwerk</div>
  <div class="row"><svg width="30" height="30" viewBox="0 0 30 30"><path d="M15 27s-8-9-8-15a8 8 0 0116 0c0 6-8 15-8 15z" fill="none" stroke="#8a8076" stroke-width="1.6"/><circle cx="15" cy="12" r="3" fill="none" stroke="#8a8076" stroke-width="1.6"/></svg><span>Lorem ipsum dolor sit amet</span></div>
  <div class="row"><svg width="30" height="30" viewBox="0 0 30 30"><path d="M8 4l5 5-3 3c2 4 4 6 8 8l3-3 5 5-3 4C13 25 5 17 4 7z" fill="none" stroke="#8a8076" stroke-width="1.6"/></svg><span>0151 – 000 472 19</span></div>
  <div class="row"><span style="width:30px;text-align:center;font-size:22px;color:var(--taupe)">@</span><span>info@pfotenwerk.de</span></div>
  <div style="display:flex;gap:22px;margin-top:40px;padding-left:6px">
    <span class="social"></span><span class="social"></span><span class="social"></span>
  </div>
</div>

<p class="legal abs">© 2021 Pfotenwerk &nbsp;&nbsp;Legal Disclaimer - Privacy Statement</p>

</body>
</html>
```